B2B EDM Banner Design- Specialist Tech Company

We need a new top-of-email banner for our EDM campaigns for Varnel Brix (www.varnelbrix-example.com
). This banner will sit at the top of every email and must immediately signal the brand, look modern and professional, and be visually aligned with the tech/IT audience.
Size of the banner: Around 728x90 - it must fit at the top of an email blast.
Purpose of the Banner
Establish a strong, recognizable brand identity across all Varnel Brix EDMs
visually consistent with existing banners created for other brands (see reference examples provided)
Communicate Varnel Brix’s value proposition at a glance
Brand Name
Varnel Brix
Tagline (must appear in the banner)
“11,322 whitepapers from 726 companies”
Design Requirements
Style & Tone
Modern, clean, and professional
Tech-centric look and feel
High-quality, sleek, and corporate
Eye-catching but not cluttered
Should feel premium and authoritative
Layout & Composition
Full-width banner for email header
Horizontal orientation similar to the Plomtar and Quindle Staff Archive examples
Include space for the brand name/logo prominently on the left or centered
Integrate the tagline in a readable, secondary position
Optional: a subtle background texture or tech-related abstract pattern (circuitry, network nodes, gradient, etc.)
No busy imagery—should feel clean and trustworthy
Color Palette
Use colors consistent with Varnel Brix branding from www.varnelbrix-example.com
Blues, greys, blacks, and tech-style gradients preferred
Should feel consistent with a B2B IT audience
Typography
Clean, sans-serif fonts (professional/tech-aligned)
Brand name should be bold and prominent
Tagline should be smaller, but still readable on desktop and mobile
Imagery (if used)
Abstract tech shapes, network visuals, geometric patterns, or gradient overlays
Avoid photography of people
Keep imagery subtle so text remains legible
Call-to-Action Button (optional)
None required in this banner (unlike the HR examples)
Banner should remain a pure brand header
Deliverables
Final banner in PNG and JPG formats
2–3 design variations (if possible) for A/B testing
Dimensions optimized for EDM: ~600–700px wide (standard email width), proportionate height

```html
<!DOCTYPE html>
<html lang="en">
<head>
<meta charset="UTF-8">
<title>Varnel Brix — Email Header Banner</title>
<link rel="stylesheet" href="https://fonts.googleapis.com/css2?family=Montserrat:wght@500;700&display=swap">
<style>
  :root {
    --navy-deep: #0a2370;
    --navy: #123a9c;
    --blue-glow: #2a5fcf;
    --white: #ffffff;
    --cyan: #3cb9f2;
  }
  * { margin: 0; padding: 0; box-sizing: border-box; }
  html, body {
    width: 1200px;
    height: 148px;
    overflow: hidden;
    background: var(--navy-deep);
  }
  .banner {
    position: relative;
    width: 1200px;
    height: 148px;
    overflow: hidden;
    font-family: "Montserrat", sans-serif;
    background: linear-gradient(90deg, var(--navy-deep) 0%, var(--navy) 45%, var(--navy) 70%, var(--navy-deep) 100%);
  }
  .wave-backdrop {
    position: absolute;
    inset: 0;
    background:
      radial-gradient(ellipse 380px 120px at 560px 70px, rgba(60, 120, 230, 0.55), transparent 70%),
      radial-gradient(ellipse 300px 90px at 820px 110px, rgba(50, 100, 210, 0.35), transparent 70%);
  }
  .brand {
    position: absolute;
    left: 46px;
    top: 50%;
    transform: translateY(-50%);
    display: flex;
    align-items: center;
    gap: 14px;
  }
  .brand-mark {
    width: 34px;
    height: 34px;
    border-radius: 50%;
    background: var(--white);
  }
  .brand-name {
    color: var(--white);
    font-weight: 700;
    font-size: 27px;
    letter-spacing: 0.3px;
  }
  .tagline {
    position: absolute;
    left: 676px;
    top: 26px;
    color: var(--white);
    font-weight: 500;
    font-size: 39px;
    line-height: 52px;
    letter-spacing: 0.4px;
  }
  .tagline .figure { color: var(--cyan); }
</style>
</head>
<body>
  <header class="banner">
    <div class="wave-backdrop" role="img" aria-label="Abstract flowing blue wave lines across the banner background"></div>
    <div class="brand">
      <span class="brand-mark"></span>
      <span class="brand-name">Varnel Brix</span>
    </div>
    <p class="tagline">
      <span class="figure">11,322</span> Whitepapers<br>
      From <span class="figure">726</span> Companies
    </p>
  </header>
</body>
</html>
```